sydney wedding photography business needs a business card design

we need a business card design for a sydney based wedding photography and videography business. our business name is :golden hour photography and video. our target clients are 24-35 yrs female. our style is candid, organic, natural, dynamic. we are a team of young photographers and videographers, and help brides to create memories that they will cherish for the rest of their lives. the logo will be provided. we want an elegant design that reflects our style, and also want to give a great impression to our clients that we are one of the best studios in sydney and our brand means quality and premium service.

Target Market(s)

bride to be, 24-35 years old, living in sydney and surrunding areas

Industry/Entity Type

Wedding Photography

Contact Information for Business Card

address: 57 marrow lane, bexton nsw 2041
mobile: 0431872056
phone: (02) 9361 2748
info@goldenhourstudio.net.au
www.goldenhourstudio.net.au
facebook:goldenhourbridals
instagram:goldenhourbridals

Font styles to use
Serif
Sans Serif

Requirements
Nice to have
• maybe add my slogan"memories beyond eternity" if the layout looks good
Should not have
• no black color, not good idea for wedding biz card

```html
<!DOCTYPE html>
<html lang="en">
<head>
<meta charset="utf-8">
<title>Golden Hour Photography and Video – Business Card</title>
<link rel="stylesheet" href="https://fonts.googleapis.com/css2?family=Open+Sans:wght@400;600;700&display=swap">
<style>
  :root {
    --backdrop: #d8d0c6;
    --card: #3b2a22;
    --card-edge: #4a372d;
    --gold: #e3aa1c;
    --gold-soft: #c4952c;
    --text-light: #f4ede4;
  }
  html, body {
    margin: 0;
    padding: 0;
    width: 1200px;
    height: 900px;
    overflow: hidden;
    background: var(--backdrop);
    font-family: "Open Sans", Arial, sans-serif;
  }
  .canvas {
    position: relative;
    width: 1200px;
    height: 900px;
  }
  .card {
    position: absolute;
    top: 300px;
    width: 520px;
    height: 300px;
    background: var(--card);
    border: 1px solid var(--card-edge);
    box-sizing: border-box;
  }
  .card--back { left: 50px; }
  .card--front { left: 630px; }

  /* Back: brand mark area, divider, contact details */
  .brand-mark {
    position: absolute;
    left: 30px;
    top: 0;
    bottom: 0;
    width: 200px;
    display: flex;
    flex-direction: column;
    align-items: center;
    justify-content: center;
    gap: 14px;
  }
  .brand-mark__dot {
    width: 22px;
    height: 22px;
    border-radius: 50%;
    background: var(--gold);
  }
  .brand-mark__name {
    color: var(--gold);
    font-weight: 700;
    font-size: 22px;
    line-height: 1.2;
    text-align: center;
  }
  .divider {
    position: absolute;
    left: 258px;
    top: 55px;
    height: 190px;
    width: 1px;
    background: linear-gradient(to bottom, transparent, var(--gold-soft), transparent);
  }
  .contact {
    position: absolute;
    left: 280px;
    top: 60px;
    right: 16px;
    color: var(--text-light);
    font-size: 13px;
    line-height: 1.3;
  }
  .contact__name {
    color: var(--gold);
    font-weight: 700;
    font-size: 16px;
    margin: 0;
  }
  .contact__role { margin: 0 0 14px; }
  .contact__address { margin: 0 0 14px; }
  .contact__list {
    list-style: none;
    margin: 0;
    padding: 0;
  }
  .contact__item {
    display: flex;
    align-items: center;
    gap: 8px;
    margin-bottom: 2px;
    white-space: nowrap;
  }
  .contact__icon {
    width: 10px;
    height: 10px;
    flex: none;
  }

  /* Front: brand name */
  .front-brand {
    position: absolute;
    inset: 0;
    display: flex;
    align-items: center;
    justify-content: center;
  }
  .front-brand__name {
    color: var(--gold);
    font-weight: 700;
    font-size: 34px;
    line-height: 1.25;
    text-align: center;
    margin: 0;
  }
</style>
</head>
<body>
<main class="canvas">

  <section class="card card--back" aria-label="Business card back">
    <div class="brand-mark">
      <span class="brand-mark__dot"></span>
      <span class="brand-mark__name">Golden Hour</span>
    </div>
    <div class="divider"></div>
    <div class="contact">
      <p class="contact__name">Oliver Reid</p>
      <p class="contact__role">Managing Director</p>
      <p class="contact__address">57 Marrow Lane,<br>Bexton NSW 2041.</p>
      <ul class="contact__list">
        <li class="contact__item">
          <svg class="contact__icon" viewBox="0 0 10 10" aria-hidden="true">
            <path d="M2 0.5 L3.8 2.6 L2.8 3.8 Q4 6.2 6.2 7.2 L7.4 6.2 L9.5 8 L8.2 9.5 Q3.5 9 0.5 1.8 Z" fill="var(--gold)"/>
          </svg>
          <span>0431 872 056</span>
        </li>
        <li class="contact__item">
          <svg class="contact__icon" viewBox="0 0 10 10" aria-hidden="true">
            <rect x="0.5" y="2" width="9" height="6.5" fill="var(--gold)"/>
            <path d="M0.5 2 L5 5.6 L9.5 2" fill="none" stroke="var(--card)" stroke-width="0.9"/>
          </svg>
          <span>info@goldenhourstudio.net.au</span>
        </li>
        <li class="contact__item">
          <svg class="contact__icon" viewBox="0 0 10 10" aria-hidden="true">
            <circle cx="5" cy="5" r="4.5" fill="var(--gold)"/>
            <path d="M0.5 5 H9.5 M5 0.5 Q2.5 5 5 9.5 M5 0.5 Q7.5 5 5 9.5" fill="none" stroke="var(--card)" stroke-width="0.7"/>
          </svg>
          <span>www.goldenhourstudio.net.au</span>
        </li>
      </ul>
    </div>
  </section>

  <section class="card card--front" aria-label="Business card front">
    <div class="front-brand">
      <p class="front-brand__name">Golden Hour<br>Photography and Video</p>
    </div>
  </section>

</main>
</body>
</html>
```